Important Solar Energy Company Needs a Stationery Design

I need a modern, attractive, corporate stationary design (letter head and business card)
Attached Company Logo

Target Market(s)

Upmarket

Industry/Entity Type

Business

Colors
ec1f27
ffffff
757575
cbcbcb
000000

```html
<!DOCTYPE html>
<html lang="en">
<head>
<meta charset="utf-8">
<title>Solariva Stationery</title>
<link href="https://fonts.googleapis.com/css2?family=Arimo:wght@400;700&display=swap" rel="stylesheet">
<style>
  :root {
    --brand-red: #ec1f27;
    --paper: #ffffff;
    --grey: #757575;
    --light-grey: #cbcbcb;
    --ink: #000000;
    --stage: #eeeeee;
    --edge: #dddddd;
  }
  html, body { margin: 0; padding: 0; overflow: hidden; }
  body {
    width: 1200px; height: 937px; position: relative;
    background: var(--stage);
    font-family: "Arimo", Arial, sans-serif; color: var(--ink);
  }
  .sheet {
    position: absolute; background: var(--paper);
    border: 1px solid var(--edge); box-sizing: border-box; overflow: hidden;
  }
  .brand { display: flex; align-items: center; white-space: nowrap; }
  .brand-dot { border-radius: 50%; background: var(--brand-red); flex: none; }
  .brand-name { font-weight: 400; color: var(--ink); letter-spacing: 0.08em; }

  /* Letterhead */
  .letterhead { left: 184px; top: 66px; width: 389px; height: 546px; }
  .letterhead .brand { position: absolute; left: 18px; top: 26px; }
  .letterhead .brand-dot { width: 38px; height: 38px; margin-right: 10px; }
  .letterhead .brand-name { font-size: 17px; }
  .letterhead .sender {
    position: absolute; right: 18px; top: 24px; text-align: right;
    font-size: 5.5px; line-height: 7px; color: var(--grey);
  }
  .letter-body {
    position: absolute; left: 38px; top: 140px; width: 300px;
    font-size: 5.6px; line-height: 7.4px; color: #444;
  }
  .letter-body p { margin: 0 0 10px; }
  .letter-body .gap { margin-bottom: 22px; }
  .signature-line { width: 32px; height: 12px; border-bottom: 1px solid #333; margin: 4px 0 6px; }

  /* Folder */
  .folder { left: 636px; top: 40px; width: 458px; height: 576px; }
  .folder .brand { position: absolute; left: 0; right: 0; top: 250px; flex-direction: column; }
  .folder .brand-dot { width: 82px; height: 82px; margin-bottom: 22px; }
  .folder .brand-name { font-size: 30px; letter-spacing: 0.12em; }

  /* Business cards */
  .card { left: 45px; width: 177px; height: 100px; }
  .card-front { top: 658px; }
  .card-back { top: 785px; height: 97px; }
  .card-front .brand { position: absolute; left: 8px; top: 8px; }
  .card-front .brand-dot { width: 16px; height: 16px; margin-right: 5px; }
  .card-front .brand-name { font-size: 8px; }
  .card-holder { position: absolute; right: 8px; top: 48px; text-align: right; }
  .card-holder .name { font-size: 7px; font-weight: 700; }
  .card-holder .role { font-size: 6px; color: var(--grey); margin-top: 1px; }
  .card-contact {
    position: absolute; left: 8px; bottom: 6px; font-size: 4px; line-height: 5px; color: var(--grey);
  }
  .card-web { position: absolute; right: 8px; bottom: 6px; font-size: 4.5px; color: var(--grey); letter-spacing: 0.1em; }
  .card-back .brand { position: absolute; left: 0; right: 0; top: 30px; justify-content: center; }
  .card-back .brand-dot { width: 20px; height: 20px; margin-right: 6px; }
  .card-back .brand-name { font-size: 10px; }
  .card-back .card-web { left: 0; right: 0; bottom: 14px; text-align: center; font-size: 7px; color: #333; }

  /* Envelopes */
  .envelope { top: 672px; width: 432px; height: 208px; }
  .envelope-front { left: 265px; }
  .envelope-front .brand { position: absolute; left: 15px; top: 22px; }
  .envelope-front .brand-dot { width: 38px; height: 38px; margin-right: 12px; }
  .envelope-front .brand-name { font-size: 16px; }
  .envelope-back { left: 737px; }
  .envelope-flap {
    position: absolute; left: 0; top: 0; width: 100%; height: 71px;
    background: var(--ink); border-radius: 0 0 60px 60px;
    display: flex; align-items: center; justify-content: center;
  }
  .envelope-flap .web { color: var(--paper); font-size: 10px; letter-spacing: 0.25em; }
</style>
</head>
<body>

<section class="sheet letterhead">
  <div class="brand"><span class="brand-dot"></span><span class="brand-name">SOLARIVA</span></div>
  <div class="sender">418 Sunfield Ave<br>Riverton TX 70112<br>555.010.2040<br>dana@solariva.com</div>
  <div class="letter-body">
    <p>July 2, 2012</p>
    <p><strong>Dear Client,</strong><br>ABC Building, def St., Country Name</p>
    <p>Is simply dummy text of the printing and typesetting industry. Lorem Ipsum has been the industry's standard dummy text ever since the 1500s, when an unknown printer took a galley of type and scrambled it to make a type specimen book. It has survived not only five centuries, but also the leap into electronic typesetting, remaining essentially unchanged. It was popularised in the 1960s with the release of Letraset sheets containing Lorem Ipsum passages, and more recently with desktop publishing software like Aldus PageMaker including versions of Lorem Ipsum.</p>
    <p class="gap">Is simply dummy text of the printing and typesetting industry. Lorem Ipsum has been the industry's standard dummy text ever since the 1500s, when an unknown printer took a galley of type and scrambled it to make.</p>
    <p>Is simply dummy text of the printing and typesetting industry. Lorem Ipsum has been the industry's standard dummy text ever since the 1500s, when an unknown printer took a galley of type and scrambled it to make a type specimen book. It has survived not only five centuries, but also the leap into electronic typesetting, remaining essentially unchanged. It was popularised in the 1960s with the release of Letraset sheets containing Lorem Ipsum passages, and more recently with desktop publishing software like Aldus PageMaker including versions of Lorem Ipsum.</p>
    <p>Best Regards,</p>
    <div class="signature-line"></div>
    <p><strong>Martin Hale</strong><br>Director<br><br>ABC Building, def St., Country Name</p>
  </div>
</section>

<section class="sheet folder">
  <div class="brand"><span class="brand-dot"></span><span class="brand-name">SOLARIVA</span></div>
</section>

<section class="sheet card card-front">
  <div class="brand"><span class="brand-dot"></span><span class="brand-name">SOLARIVA</span></div>
  <div class="card-holder"><div class="name">Dana Whitfield</div><div class="role">Owner</div></div>
  <div class="card-contact">555.010.2040<br>dana@solariva.com<br>418 Sunfield Ave Riverton TX 70112</div>
  <div class="card-web">www.solariva.com</div>
</section>

<section class="sheet card card-back">
  <div class="brand"><span class="brand-dot"></span><span class="brand-name">SOLARIVA</span></div>
  <div class="card-web">www.solariva.com</div>
</section>

<section class="sheet envelope envelope-front">
  <div class="brand"><span class="brand-dot"></span><span class="brand-name">SOLARIVA</span></div>
</section>

<section class="sheet envelope envelope-back">
  <div class="envelope-flap"><span class="web">www.solariva.com</span></div>
</section>

</body>
</html>
```